Brochure Design Project law firm

we require a print brochure for marketing. the information is contained on our website www.brindlecourt.com.au
we need to appeal to smash repairers who do third party claims. which means, where a person has had a car accident where it is not their fault they want their car fixed by the smash repairer who agrees to do the repairs and then claims the money from the insurer directly.

we will need a logo and business cards too.

Industry/Entity Type

Law Firm

Requirements
Must have
• pictures, law firm and smash repairer related.

```html
<!DOCTYPE html>
<html lang="en">
<head>
<meta charset="utf-8">
<title>Brindle Court – Smash Repair Law Flyer</title>
<link href="https://fonts.googleapis.com/css2?family=Libre+Franklin:wght@300;400;500;600;700&display=swap" rel="stylesheet">
<style>
  :root {
    --brand-red: #a91d26;
    --band-red-dark: #7e0f15;
    --band-red-light: #b51f28;
    --ink: #1a1a1a;
    --paper: #ffffff;
    --footer-black: #0d0d0d;
    --rule: #b5b5b5;
  }
  * { margin: 0; padding: 0; box-sizing: border-box; }
  html, body {
    width: 1080px; height: 1200px; overflow: hidden;
    background: var(--paper);
    font-family: "Libre Franklin", Arial, sans-serif;
  }
  .flyer { position: relative; width: 1080px; height: 1200px; background: var(--paper); }

  .masthead {
    position: absolute; top: 80px; left: 80px; right: 80px;
    display: flex; justify-content: space-between; align-items: flex-start;
  }
  .brand { display: flex; align-items: center; gap: 16px; margin-top: 14px; }
  .brand-square { width: 24px; height: 24px; background: var(--brand-red); }
  .brand-name {
    color: var(--brand-red); font-weight: 400; font-size: 54px; line-height: 1;
  }
  .specialty {
    color: var(--brand-red); font-weight: 300; font-size: 34px; line-height: 1.22;
    text-align: right;
  }

  .hero-visual { position: absolute; top: 330px; left: 80px; width: 920px; height: 400px; }

  .claim-band {
    position: absolute; top: 740px; left: 0; width: 1080px; height: 130px;
    background: linear-gradient(180deg, var(--band-red-light) 0%, var(--band-red-dark) 100%);
    color: var(--paper); display: flex; align-items: center; padding: 0 70px;
  }
  .claim-band p { font-weight: 300; font-size: 37px; line-height: 1.3; }

  .details { position: absolute; top: 892px; left: 70px; right: 70px; display: flex; }
  .contact { width: 280px; color: var(--brand-red); font-size: 15px; line-height: 1.35; }
  .contact h2 { font-size: 17px; font-weight: 700; margin-bottom: 9px; }
  .contact p { margin-bottom: 7px; font-weight: 400; }
  .contact p:last-child { margin-bottom: 0; }
  .contact strong { font-weight: 700; }
  .divider { width: 1px; background: var(--rule); margin: 0 28px; height: 200px; }
  .pitch { flex: 1; color: var(--ink); font-size: 15.5px; line-height: 1.55; }
  .pitch .lead { font-weight: 600; margin-bottom: 8px; }
  .pitch p { margin-bottom: 8px; }
  .pitch .call { font-weight: 500; }
  .pitch .call strong { font-weight: 700; }

  .site-footer {
    position: absolute; bottom: 0; left: 0; width: 1080px; height: 74px;
    background: linear-gradient(180deg, #2a2a2a 0%, var(--footer-black) 60%);
    color: var(--paper); display: flex; align-items: center; justify-content: center;
    font-weight: 700; font-size: 19px; letter-spacing: 0.3px;
  }
</style>
</head>
<body>
<main class="flyer">
  <header class="masthead">
    <div class="brand">
      <span class="brand-square" aria-hidden="true"></span>
      <span class="brand-name">Brindle Court</span>
    </div>
    <div class="specialty">Highly<br>Experienced<br>in Smash<br>Repair Law</div>
  </header>

  <svg class="hero-visual" role="img" aria-label="Photograph of a silver convertible car with a crushed, crash-damaged front end" viewBox="0 0 920 400" preserveAspectRatio="none">
    <defs>
      <radialGradient id="heroTone" cx="50%" cy="55%" r="60%">
        <stop offset="0%" stop-color="#9a9a9c"/>
        <stop offset="55%" stop-color="#d4d4d6"/>
        <stop offset="100%" stop-color="#ffffff"/>
      </radialGradient>
    </defs>
    <rect width="920" height="400" fill="url(#heroTone)"/>
  </svg>

  <section class="claim-band">
    <p>We provide the best solutions on recovery of<br>third party insurance claims for smash repairers</p>
  </section>

  <section class="details">
    <div class="contact">
      <h2>CONTACT:</h2>
      <p><strong>Phone:</strong> 0491 570 156</p>
      <p><strong>Fax:</strong> 02 5550 1234</p>
      <p>118 Kellett Lane,<br>HAYMARKET, NSW 2001</p>
      <p>P.O. Box 4470, Market Square,<br>NSW 2002</p>
      <p><strong>Email:</strong> marcus@brindlecourt.com.au</p>
    </div>
    <div class="divider"></div>
    <div class="pitch">
      <p class="lead">We focus purely on third party recovery claims for smash repairers.</p>
      <p>We take the fight the big insurers to achieve the best results and ensure your rights are secured and to maximise profits. We have state of the art systems and a team of dedicated professionals who will achieve the best results and ensure that if a client comes to you, they stay with you so you can do what you do best, fix cars!</p>
      <p class="call">If you want the best solution <strong>call Marcus on 0491 570 156 to arrange a free, no obligation meeting with one of our specialist lawyers.</strong></p>
    </div>
  </section>

  <footer class="site-footer">www.brindlecourt.com.au</footer>
</main>
</body>
</html>
```